Billboard design - consider what a billboard is

Design a billboard using my logo - Billboard is 6m x 3m
A Billboard is advertising for my company that is on a big sign.

Has to be clean and easy to read, and ideally highlights that we are Residential and Commercial builders.

Keep it clean and easy to read

The contact number for the board is

022 583 7092
www.harbourframeworks.co.nz
info@harbourframeworks.co.nz

Doesnt have to have all contact details if it doesnt fit

Has to catch peoples attention to contact us if they need a builder

Can you please change the sign to be all white writing, with black background ?
Updates

Please consider what a billboard is...

The design needs to be suitable for a billboard..

Target Market(s)

people driving past

Industry/Entity Type

Construction

Logo Text

Wellington Builder, website email address, contact number

Colors
0054AA
0677BA
7BADD7
CADEEF
E8F1F8

Requirements
Must have
• Easy to read
Nice to have
• easy to read, can clearly see contact details

```html
<!DOCTYPE html>
<html lang="en">
<head>
<meta charset="UTF-8">
<title>Harbour Frameworks – Wellington Builder Billboard</title>
<link rel="stylesheet" href="https://fonts.googleapis.com/css2?family=Fredoka:wght@500;600&display=swap">
<style>
  :root {
    --brand-blue: #558cce;
    --board-black: #000000;
    --text-white: #ffffff;
    --stage-bg: #e4edf6;
  }
  * { margin: 0; padding: 0; box-sizing: border-box; }
  html, body {
    width: 1200px;
    height: 1000px;
    overflow: hidden;
    background: var(--stage-bg);
    font-family: "Fredoka", sans-serif;
  }
  .billboard {
    position: absolute;
    left: 50px;
    top: 225px;
    width: 1100px;
    height: 549px;
    background: var(--board-black);
    color: var(--text-white);
  }
  .brand {
    position: absolute;
    left: 80px;
    top: 45px;
    width: 420px;
    height: 190px;
    display: flex;
    align-items: center;
    gap: 20px;
  }
  .brand-square {
    flex: none;
    width: 56px;
    height: 140px;
    background: var(--brand-blue);
  }
  .brand-name {
    color: var(--text-white);
    font-weight: 600;
    font-size: 54px;
    line-height: 1.05;
  }
  .headline {
    position: absolute;
    left: 540px;
    top: 68px;
    width: 520px;
    text-align: center;
    color: var(--text-white);
    font-weight: 600;
  }
  .headline-place {
    display: block;
    font-size: 78px;
    line-height: 1;
    letter-spacing: 1px;
  }
  .headline-trade {
    display: block;
    margin-top: 14px;
    font-size: 38px;
    line-height: 1;
    letter-spacing: 14px;
    padding-left: 14px;
  }
  .headline-services {
    display: block;
    margin-top: 16px;
    font-size: 24px;
    line-height: 1;
    letter-spacing: 3px;
    font-weight: 500;
  }
  .call-label {
    position: absolute;
    left: 0;
    width: 100%;
    top: 278px;
    text-align: center;
    color: var(--text-white);
    font-weight: 600;
    font-size: 46px;
    line-height: 1;
  }
  .phone-pill {
    position: absolute;
    left: 343px;
    top: 334px;
    width: 414px;
    height: 90px;
    border-radius: 45px;
    background: var(--brand-blue);
    color: var(--text-white);
    font-weight: 600;
    font-size: 56px;
    line-height: 90px;
    text-align: center;
    letter-spacing: 1px;
  }
  .contact-list {
    position: absolute;
    left: 0;
    width: 100%;
    top: 442px;
    list-style: none;
    display: flex;
    flex-direction: column;
    align-items: center;
    gap: 10px;
    color: var(--text-white);
    font-weight: 600;
    font-size: 26px;
    line-height: 34px;
  }
  .contact-item {
    display: flex;
    align-items: center;
    gap: 18px;
  }
  .contact-icon {
    width: 38px;
    height: 30px;
    flex: none;
  }
</style>
</head>
<body>
  <main class="billboard">
    <div class="brand">
      <span class="brand-square" aria-hidden="true"></span>
      <span class="brand-name">Harbour<br>Frameworks</span>
    </div>

    <h1 class="headline">
      <span class="headline-place">WELLINGTON</span>
      <span class="headline-trade">BUILDER</span>
      <span class="headline-services">RESIDENTIAL &amp; COMMERCIAL</span>
    </h1>

    <p class="call-label">CALL NOW</p>
    <p class="phone-pill">022 583 7092</p>

    <ul class="contact-list">
      <li class="contact-item">
        <svg class="contact-icon" viewBox="0 0 38 30" aria-hidden="true">
          <rect x="2" y="3" width="34" height="24" fill="none" stroke="#ffffff" stroke-width="3"/>
          <polyline points="2,3 19,17 36,3" fill="none" stroke="#ffffff" stroke-width="3"/>
        </svg>
        <span>info@harbourframeworks.co.nz</span>
      </li>
      <li class="contact-item">
        <svg class="contact-icon" viewBox="0 0 38 30" aria-hidden="true">
          <circle cx="19" cy="15" r="13" fill="#ffffff"/>
          <g fill="none" stroke="#000000" stroke-width="1.6">
            <ellipse cx="19" cy="15" rx="5.5" ry="13"/>
            <line x1="6" y1="15" x2="32" y2="15"/>
            <line x1="9" y1="8" x2="29" y2="8"/>
            <line x1="9" y1="22" x2="29" y2="22"/>
            <line x1="19" y1="2" x2="19" y2="28"/>
          </g>
        </svg>
        <span>www.harbourframeworks.co.nz</span>
      </li>
    </ul>
  </main>
</body>
</html>
```